2026 Kelvar Montra medium roof

Van montra logo wrap, construction company Bright Oak Renovations LLC

Target Market(s)

More customers

Industry/Entity Type

License contractor, remodeling, construction

Colors

Designer to choose colors to be used in the design.

Requirements
Must have
• House logo, jobs I offer, phone number,, license & insured , KLR acquitted business,
Nice to have
• I would like to have the KLR logo in lower right bottom of van

```html
<!DOCTYPE html>
<html lang="en">
<head>
<meta charset="utf-8">
<title>Bright Oak Renovations LLC – Kelvar Montra Wrap</title>
<link href="https://fonts.googleapis.com/css2?family=Oswald:wght@600;700&family=Montserrat:wght@500;600;700&display=swap" rel="stylesheet">
<style>
:root{
  --navy:#0f2a4a;
  --blue:#1d4f8c;
  --gray:#5b5f66;
  --black:#1c1d1f;
  --white:#ffffff;
  --bg:#e6e7e9;
  --house-dusk:#2b3f5c;
  --house-warm:#b07a45;
  --lawn:#4f6b35;
}
*{margin:0;padding:0;box-sizing:border-box}
html,body{width:1200px;height:800px;overflow:hidden;background:var(--bg)}
.canvas{position:relative;width:1200px;height:800px;font-family:'Montserrat',sans-serif}
.panel{position:absolute;overflow:hidden}
.panel svg.panel-art{position:absolute;inset:0;width:100%;height:100%}
.abs{position:absolute}
.wordmark{font-family:'Oswald',sans-serif;font-weight:700;color:var(--navy);line-height:1;letter-spacing:.5px}
.subline{font-family:'Montserrat',sans-serif;font-weight:500;color:var(--gray);letter-spacing:4px;line-height:1}
.tagline{background:var(--navy);color:var(--white);font-weight:700;letter-spacing:1.5px;line-height:1;text-align:center}
.logo-mark{display:flex;align-items:center;gap:8px}
.logo-square{background:var(--navy);flex:none}
.logo-name{font-family:'Oswald',sans-serif;font-weight:700;color:var(--navy);line-height:1}

/* side */
.side{left:30px;top:30px;width:1140px;height:410px}
.side .logo-mark{left:300px;top:44px;flex-direction:column;align-items:flex-start;gap:6px}
.side .logo-square{width:62px;height:62px}
.side .logo-name{font-size:16px}
.side .wordmark{left:420px;top:40px;font-size:66px}
.side .subline{left:423px;top:116px;font-size:27px}
.side .tagline{left:423px;top:153px;width:392px;font-size:17px;padding:6px 0}
.services{left:292px;top:212px;display:flex;gap:4px}
.service{width:80px;text-align:center;color:var(--navy);font-size:10px;font-weight:700;line-height:1.25}
.service svg{display:block;margin:0 auto 6px;width:30px;height:30px}
.phone{display:flex;align-items:center;gap:14px;color:var(--white);font-weight:700}
.side .phone{left:370px;top:319px;font-size:44px}
.side .phone svg{width:40px;height:40px}
.licensed{color:var(--white);font-weight:700;font-size:11px;text-align:center;line-height:1.3}
.side .licensed{left:150px;top:150px;width:110px}
.side .licensed .logo-square{width:30px;height:30px;background:var(--white);margin:0 auto 8px}
.badge{background:var(--navy);border:2px solid var(--white);border-radius:4px}
.side .badge{left:992px;top:318px;width:130px;height:56px}

/* front */
.front{left:30px;top:470px;width:300px;height:300px;background:var(--white)}
.front .logo-mark{left:0;right:0;top:92px;justify-content:center}
.front .logo-square{width:26px;height:26px}
.front .logo-name{font-size:15px}
.front .wordmark{left:0;right:0;top:126px;text-align:center;font-size:24px}
.front .subline{left:0;right:0;top:154px;text-align:center;font-size:11px;letter-spacing:2.5px}

/* rear */
.rear{left:350px;top:470px;width:300px;height:300px;background:var(--white)}
.rear .logo-mark{left:0;right:0;top:22px;justify-content:center}
.rear .logo-square{width:34px;height:34px}
.rear .logo-name{font-size:16px}
.rear .wordmark{left:0;right:0;top:66px;text-align:center;font-size:30px}
.rear .subline{left:0;right:0;top:100px;text-align:center;font-size:14px;letter-spacing:3px}
.rear .tagline{left:45px;top:122px;width:210px;font-size:10.5px;padding:5px 0}
.rear .phone{left:0;right:0;top:160px;justify-content:center;color:var(--navy);font-size:26px;gap:8px}
.rear .phone svg{width:24px;height:24px}
.rear .licensed{left:0;right:0;top:204px;color:var(--navy);font-size:11px}
.rear .badge{left:110px;top:254px;width:80px;height:34px}

/* roof */
.roof{left:670px;top:470px;width:500px;height:300px;background:var(--blue);border-radius:6px}
.roof .logo-mark{left:60px;top:110px}
.roof .logo-square{width:80px;height:80px;background:var(--white)}
.roof .wordmark{left:180px;top:92px;font-size:46px;color:var(--white)}
.roof .subline{left:182px;top:146px;font-size:19px;color:var(--white);letter-spacing:3.5px}
.roof .rule{left:182px;top:174px;width:270px;height:2px;background:var(--white)}
.roof .tagline{left:182px;top:184px;background:none;font-size:13px;letter-spacing:1px;text-align:left}
</style>
</head>
<body>
<main class="canvas">

  <!-- Side wrap -->
  <section class="panel side" aria-label="Side wrap">
    <svg class="panel-art" viewBox="0 0 1140 410" preserveAspectRatio="none">
      <defs>
        <linearGradient id="houseTone" x1="0" y1="0" x2="0" y2="1">
          <stop offset="0" stop-color="var(--house-dusk)"/>
          <stop offset=".55" stop-color="var(--house-warm)"/>
          <stop offset="1" stop-color="var(--lawn)"/>
        </linearGradient>
      </defs>
      <rect width="1140" height="410" fill="var(--white)"/>
      <polygon points="0,0 265,0 265,215 150,410 0,410" fill="var(--black)"/>
      <polygon points="175,410 300,205 335,205 245,310 1140,310 1140,410" fill="var(--blue)"/>
      <rect x="0" y="380" width="1140" height="30" fill="var(--black)"/>
      <polygon points="775,310 905,40 1140,0 1140,310" fill="var(--blue)"/>
      <polygon class="photo" role="img" aria-label="Photo of a modern two-storey home at dusk with lit windows and landscaped lawn" points="800,310 925,62 1140,22 1140,380 800,380" fill="url(#houseTone)"/>
    </svg>

    <div class="abs licensed"><div class="logo-square"></div>LICENSED &amp;<br>INSURED</div>

    <div class="abs logo-mark"><div class="logo-square"></div><span class="logo-name">BRIGHT OAK</span></div>
    <div class="abs wordmark">BRIGHT OAK</div>
    <div class="abs subline">RENOVATIONS LLC</div>
    <div class="abs tagline">REMODELING &amp; CONSTRUCTION</div>

    <div class="abs services">
      <div class="service"><svg viewBox="0 0 30 30"><circle cx="15" cy="15" r="12" fill="none" stroke="var(--navy)" stroke-width="2"/></svg>KITCHENS &amp;<br>BATHROOMS</div>
      <div class="service"><svg viewBox="0 0 30 30"><circle cx="15" cy="15" r="12" fill="none" stroke="var(--navy)" stroke-width="2"/></svg>ROOFING &amp;<br>SIDING</div>
      <div class="service"><svg viewBox="0 0 30 30"><circle cx="15" cy="15" r="12" fill="none" stroke="var(--navy)" stroke-width="2"/></svg>PAINTING &amp;<br>DRYWALL</div>
      <div class="service"><svg viewBox="0 0 30 30"><circle cx="15" cy="15" r="12" fill="none" stroke="var(--navy)" stroke-width="2"/></svg>FLOORING</div>
      <div class="service"><svg viewBox="0 0 30 30"><circle cx="15" cy="15" r="12" fill="none" stroke="var(--navy)" stroke-width="2"/></svg>DECKS &amp;<br>FENCES</div>
      <div class="service"><svg viewBox="0 0 30 30"><circle cx="15" cy="15" r="12" fill="none" stroke="var(--navy)" stroke-width="2"/></svg>PLUMBING &amp;<br>ELECTRICAL</div>
    </div>

    <div class="abs phone">
      <svg viewBox="0 0 40 40"><circle cx="20" cy="20" r="18" fill="none" stroke="currentColor" stroke-width="3"/><path d="M13 11c2-1 3 0 4 3l1 3-2 2c1 3 3 5 6 6l2-2 3 1c3 1 4 2 3 4-1 2-3 3-5 3-8-1-14-7-15-15 0-2 1-4 3-5z" fill="currentColor"/></svg>
      (555) 014-2738
    </div>

    <div class="abs badge" aria-label="Accreditation badge"></div>
  </section>

  <!-- Front hood -->
  <section class="panel front" aria-label="Front wrap">
    <svg class="panel-art" viewBox="0 0 300 300" preserveAspectRatio="none">
      <polygon points="0,150 40,110 40,200 0,230" fill="var(--blue)"/>
      <polygon points="300,150 260,110 260,200 300,230" fill="var(--blue)"/>
      <rect x="0" y="230" width="300" height="70" fill="var(--black)"/>
    </svg>
    <div class="abs logo-mark"><div class="logo-square"></div><span class="logo-name">BRIGHT OAK</span></div>
    <div class="abs wordmark">BRIGHT OAK</div>
    <div class="abs subline">RENOVATIONS LLC</div>
  </section>

  <!-- Rear doors -->
  <section class="panel rear" aria-label="Rear wrap">
    <svg class="panel-art" viewBox="0 0 300 300" preserveAspectRatio="none">
      <rect x="0" y="240" width="300" height="60" fill="var(--black)"/>
    </svg>
    <div class="abs logo-mark"><div class="logo-square"></div><span class="logo-name">BRIGHT OAK</span></div>
    <div class="abs wordmark">BRIGHT OAK</div>
    <div class="abs subline">RENOVATIONS LLC</div>
    <div class="abs tagline">REMODELING &amp; CONSTRUCTION</div>
    <div class="abs phone">
      <svg viewBox="0 0 40 40"><circle cx="20" cy="20" r="20" fill="currentColor"/><path d="M13 11c2-1 3 0 4 3l1 3-2 2c1 3 3 5 6 6l2-2 3 1c3 1 4 2 3 4-1 2-3 3-5 3-8-1-14-7-15-15 0-2 1-4 3-5z" fill="var(--white)"/></svg>
      (555) 014-2738
    </div>
    <div class="abs licensed">LICENSED &amp; INSURED</div>
    <div class="abs badge" aria-label="Accreditation badge"></div>
  </section>

  <!-- Roof -->
  <section class="panel roof" aria-label="Roof wrap">
    <div class="abs logo-mark"><div class="logo-square"></div></div>
    <div class="abs wordmark">BRIGHT OAK</div>
    <div class="abs subline">RENOVATIONS LLC</div>
    <div class="abs rule"></div>
    <div class="abs tagline">REMODELING &amp; CONSTRUCTION</div>
  </section>

</main>
</body>
</html>
```